Stationary for I.T. company
DuskVale
Stationary for I.T. company - Information Technology
Creative Brief
Bright & Fun-filled
Ray Olsen
Director
PO Box 4172 Marlow ACT 2913
ops@duskva.le
duskva.le
Eye catching - display the DuskVale logo with either the red N with the white text or the white only logo on a background with either bold colours, dark greys or black. Open to other concepts or suggestions if they are eye catching
brimlow brimlow
Thank you everyone for your efforts. We may ask a couple more questons to relevant designers - but we plan to decide in the next 24 to 48 hours. Thanks again.
Thanks everyone for your submissions so far.. 266 designs is much much more than we were expecting. To help everyone understand where we are going and what we are looking for we will start eliminating some designs tonight. With that, we will probably start to give out a couple (maybe 3) 5 star ratings. These will indicate the current leading designs. We will probably also redo most of the star ratings out there to better give designers a better understanding of what we like. Please note that there is several people looking at these designs, so star rating may go up and down a little... but be assured if it has stars, we like it, or like some concepts in it.
We will aim to provide every designer feedback and stars (so yes - it may look like we rate a lot of things highly). 4 stars will generally be used to indicate the favorite submission of a designer, and 5 will only be used when we start eliminating designs.
tallfern tallfern
Check your private messages...
Also looking for letter head, invoice, envelope, notepad templates, presentation folder in addition to business card design. Thanks.
Amendment to the design brief - we will also accept a white background for the back of the business card

```html
<!DOCTYPE html>
<html lang="en">
<head>
<meta charset="utf-8">
<title>DuskVale Stationery</title>
<link rel="stylesheet" href="https://fonts.googleapis.com/css2?family=Roboto:wght@400;700&display=swap">
<style>
:root{
  --stage:#7b7b7b;
  --paper:#ffffff;
  --red:#d0121f;
  --red-dark:#8e0610;
  --red-deep:#5e0309;
  --ink:#3a3a3a;
  --muted:#9a9a9a;
  --faint:#f3e3e4;
}
*{box-sizing:border-box;margin:0;padding:0}
html,body{width:1200px;height:365px;overflow:hidden;background:var(--stage);font-family:"Roboto",Arial,sans-serif}
.canvas{position:relative;width:1200px;height:365px}
.piece{position:absolute;background:var(--paper);overflow:hidden}
.brand{display:flex;align-items:center;gap:4px;font-weight:700;color:var(--ink);white-space:nowrap}
.brand .dot{display:inline-block;border-radius:50%;background:var(--red)}
.brand.light{color:var(--paper)}
.brand.light .dot{background:var(--paper)}
.red-band{position:absolute;left:0;right:0;background:linear-gradient(90deg,var(--red-dark),var(--red) 60%,var(--red-dark))}
.swoosh{position:absolute;background:radial-gradient(circle at 40% 40%,#f4f4f4,#c8c8c8 45%,var(--red) 46%,var(--red-dark) 80%);border-radius:50%}
.watermark{position:absolute;border-radius:50%;background:radial-gradient(circle,var(--faint),rgba(243,227,228,0) 70%)}
.small{font-size:4px;line-height:6px;color:var(--ink)}
.small.light{color:var(--paper)}

/* business cards */
.card{left:10px;width:106px;height:52px}
.card-white-1{top:100px}
.card-red-1{top:160px;background:linear-gradient(135deg,var(--red),var(--red-dark))}
.card-white-2{top:220px}
.card-red-2{top:280px;background:linear-gradient(135deg,var(--red),var(--red-dark))}
.card .red-band{bottom:0;height:12px}
.card .brand{position:absolute;left:8px;top:10px;font-size:8px}
.card .small{position:absolute;left:8px;top:24px}

/* letterheads */
.letterhead{top:41px;width:180px;height:283px}
.letterhead-1{left:163px}
.letterhead-2{left:365px}
.letterhead .watermark{left:30px;top:80px;width:120px;height:120px}
.letterhead .red-band{bottom:18px;height:22px}
.letterhead .brand{position:absolute;right:10px;bottom:24px;font-size:6px;color:var(--paper)}
.letterhead .brand .dot{background:var(--paper)}
.letterhead .header-info{position:absolute;right:12px;top:16px;text-align:right}
.letterhead .footer-info{position:absolute;left:10px;bottom:26px}

/* compliment slip */
.slip{left:569px;top:41px;width:127px;height:50px}
.slip .red-band{bottom:0;height:10px}
.slip .swoosh{left:4px;top:4px;width:26px;height:26px}
.slip .brand{position:absolute;left:34px;top:10px;font-size:6px}
.slip .small{position:absolute;left:34px;top:20px;font-size:3px;line-height:4px}

/* envelopes */
.envelope-front{left:569px;top:106px;width:127px;height:98px}
.envelope-front .swoosh{left:6px;top:6px;width:22px;height:22px}
.envelope-front .brand{position:absolute;left:32px;top:12px;font-size:6px}
.envelope-front .small{position:absolute;left:32px;top:22px;font-size:3px;line-height:4px}
.envelope-front .red-band{bottom:0;height:22px}
.envelope-back{left:569px;top:216px;width:127px;height:101px;background:transparent}
.envelope-back svg{position:absolute;inset:0}

/* folder */
.folder{left:823px;top:41px;width:365px;height:295px;background:var(--red-dark)}
.folder-inside{position:absolute;left:0;top:0;width:170px;height:295px;background:linear-gradient(180deg,#e6e6e6,#bdbdbd)}
.folder-cover{position:absolute;left:170px;top:0;width:195px;height:295px;background:linear-gradient(160deg,var(--red),var(--red-dark))}
.folder .swoosh-large{position:absolute;left:60px;top:10px;width:200px;height:200px;border-radius:50%;background:radial-gradient(circle at 45% 45%,#f6f6f6,#bcbcbc 40%,var(--red) 42%,var(--red-deep) 85%)}
.folder .brand{position:absolute;left:240px;top:70px;font-size:14px}
.folder .brand .dot{width:14px;height:14px}
.folder-pocket{position:absolute;left:0;bottom:0;width:170px;height:110px;background:var(--paper)}
.folder-pocket .small{position:absolute;left:12px;top:16px}
.folder-cover-band{position:absolute;left:170px;right:0;top:192px;height:28px;background:var(--paper)}
</style>
</head>
<body>
<main class="canvas">

  <!-- business cards -->
  <section class="piece card card-white-1">
    <div class="brand"><span class="dot" style="width:8px;height:8px"></span>DuskVale</div>
    <p class="small">Ray Olsen · Director<br>ops@duskva.le</p>
    <div class="red-band"></div>
  </section>
  <section class="piece card card-red-1">
    <div class="swoosh" role="img" aria-label="Large red and white curved brand decoration" style="left:50px;top:-10px;width:70px;height:70px"></div>
    <div class="brand light"><span class="dot" style="width:8px;height:8px"></span>DuskVale</div>
  </section>
  <section class="piece card card-white-2">
    <div class="brand"><span class="dot" style="width:8px;height:8px"></span>DuskVale</div>
    <p class="small">PO Box 4172 Marlow ACT 2913<br>duskva.le</p>
    <div class="red-band"></div>
  </section>
  <section class="piece card card-red-2">
    <div class="swoosh" role="img" aria-label="Large red and white curved brand decoration" style="left:50px;top:-10px;width:70px;height:70px"></div>
    <div class="brand light"><span class="dot" style="width:8px;height:8px"></span>DuskVale</div>
  </section>

  <!-- letterheads -->
  <section class="piece letterhead letterhead-1">
    <div class="watermark" role="img" aria-label="Faint brand decoration"></div>
    <div class="red-band"></div>
    <div class="brand"><span class="dot" style="width:6px;height:6px"></span>DuskVale</div>
  </section>
  <section class="piece letterhead letterhead-2">
    <p class="small header-info">PO Box 4172 Marlow ACT 2913<br>ops@duskva.le<br>duskva.le</p>
    <div class="watermark" role="img" aria-label="Faint brand decoration"></div>
    <div class="red-band"></div>
    <div class="brand"><span class="dot" style="width:6px;height:6px"></span>DuskVale</div>
  </section>

  <!-- compliment slip -->
  <section class="piece slip">
    <div class="swoosh" role="img" aria-label="Red and white curved brand decoration"></div>
    <div class="brand">DuskVale</div>
    <p class="small">ops@duskva.le · duskva.le</p>
    <div class="red-band"></div>
  </section>

  <!-- envelope front -->
  <section class="piece envelope-front">
    <div class="swoosh" role="img" aria-label="Red and white curved brand decoration"></div>
    <div class="brand">DuskVale</div>
    <p class="small">PO Box 4172 Marlow ACT 2913</p>
    <div class="red-band"></div>
  </section>

  <!-- envelope back -->
  <section class="piece envelope-back">
    <svg width="127" height="101" viewBox="0 0 127 101">
      <rect width="127" height="101" fill="#ffffff"/>
      <polygon points="0,0 127,0 127,30 63.5,58 0,30" fill="#c0101c"/>
      <polygon points="0,0 127,0 127,20 63.5,46 0,20" fill="#8e0610"/>
      <circle cx="63.5" cy="42" r="6" fill="#ffffff"/>
    </svg>
  </section>

  <!-- presentation folder -->
  <section class="piece folder">
    <div class="folder-inside"></div>
    <div class="folder-cover"></div>
    <div class="swoosh-large" role="img" aria-label="Large red and white curved brand decoration spanning the folder"></div>
    <div class="folder-cover-band"></div>
    <div class="folder-pocket">
      <p class="small">Ray Olsen<br>PO Box 4172 Marlow ACT 2913<br>ops@duskva.le<br>duskva.le</p>
    </div>
    <div class="brand"><span class="dot"></span>DuskVale</div>
  </section>

</main>
</body>
</html>
```